Looking for a cool & simple business-card-design for digital agency

Hi!

We are a web agency that offers Reputation Management, Vextra & Seo Services and software development. We like cool things, we like innovative styles.

We have uploaded our logo.

Project Deadline Extended Reason: Client does not want any designs with the colorful logo. Please send us submissions ONLY with the blac and white logo. What the client would like to see:1) Back of the card: is a silver logo on a black background2) front of the card with all the data, please use white background and black logo thank you Added Friday, May 8, 2015

```html
<!DOCTYPE html>
<html lang="de">
<head>
<meta charset="utf-8">
<title>Nordlicht AG – Business Card</title>
<link rel="stylesheet" href="https://fonts.googleapis.com/css2?family=Lato:wght@400;700;900&display=swap">
<style>
  :root {
    --stage: #4a4038;
    --card-black: #050505;
    --card-white: #ffffff;
    --ink: #151515;
    --silver: #c9c9c9;
    --white: #ffffff;
    --rule: #1a1a1a;
  }
  * { margin: 0; padding: 0; box-sizing: border-box; }
  html, body {
    width: 1200px; height: 905px; overflow: hidden;
    background: var(--stage);
    font-family: "Lato", Arial, sans-serif;
  }
  .stage { position: relative; width: 1200px; height: 905px; }
  .card {
    position: absolute; left: 290px; width: 620px; height: 354px;
    box-shadow: 0 10px 24px rgba(0,0,0,.45);
  }
  .card--back { top: 80px; background: var(--card-black); }
  .card--front { top: 494px; background: var(--card-white); }

  .brand { position: absolute; display: flex; align-items: center; gap: 14px; }
  .brand__mark { width: 34px; height: 34px; flex: none; }
  .brand__name {
    font-family: "Lato", Arial, sans-serif; font-weight: 900;
    font-size: 46px; line-height: 1;
  }

  .card--back .brand { left: 108px; top: 102px; }
  .card--back .brand__mark { background: var(--silver); }
  .card--back .brand__name { color: var(--silver); }
  .services {
    position: absolute; left: 0; right: 0; top: 196px;
    text-align: center; color: var(--white);
    font-weight: 700; font-size: 20px; line-height: 1.3;
  }

  .card--front .brand { left: 96px; top: 78px; }
  .card--front .brand__mark { background: var(--ink); }
  .card--front .brand__name { color: var(--ink); }

  .person {
    position: absolute; right: 340px; top: 236px; text-align: right; color: var(--ink);
  }
  .person__name { font-weight: 900; font-size: 21px; }
  .person__role { font-size: 19px; margin-top: 2px; }
  .divider {
    position: absolute; left: 296px; top: 164px; width: 2px; height: 122px;
    background: var(--rule);
  }
  .contacts {
    position: absolute; left: 316px; top: 162px; list-style: none;
    color: var(--ink); font-size: 19px; line-height: 1.4;
  }
  .contacts li { display: flex; align-items: center; gap: 8px; }
  .contacts svg { width: 16px; height: 16px; flex: none; }
</style>
</head>
<body>
<main class="stage">
  <section class="card card--back" aria-label="Card back">
    <div class="brand">
      <span class="brand__mark"></span>
      <span class="brand__name">Nordlicht AG</span>
    </div>
    <p class="services">Reputation Management<br>Vextra &amp; Seo Services<br>Software development.</p>
  </section>

  <section class="card card--front" aria-label="Card front">
    <div class="brand">
      <span class="brand__mark"></span>
      <span class="brand__name">Nordlicht AG</span>
    </div>
    <div class="person">
      <p class="person__name">Lena Brandt</p>
      <p class="person__role">Director</p>
    </div>
    <span class="divider"></span>
    <ul class="contacts">
      <li><svg viewBox="0 0 16 16" aria-hidden="true"><path d="M1 5c0-2 2-3 7-3s7 1 7 3v1h-3V5H4v1H1z M3 7h10l1 7H2z" fill="var(--ink)"/><circle cx="8" cy="10.5" r="2" fill="var(--card-white)"/></svg>040 512 7781</li>
      <li><svg viewBox="0 0 16 16" aria-hidden="true"><rect x="4" y="1" width="8" height="14" rx="1.5" fill="none" stroke="var(--ink)" stroke-width="1.6"/><circle cx="8" cy="12.5" r="0.9" fill="var(--ink)"/></svg>176 2093 418</li>
      <li><svg viewBox="0 0 16 16" aria-hidden="true"><rect x="1" y="3" width="14" height="10" fill="var(--ink)"/><path d="M1.5 3.5 8 9l6.5-5.5" fill="none" stroke="var(--card-white)" stroke-width="1.2"/></svg>info@nordlichtag.com</li>
      <li><svg viewBox="0 0 16 16" aria-hidden="true"><g fill="none" stroke="var(--ink)" stroke-width="1.3"><circle cx="8" cy="8" r="6.5"/><ellipse cx="8" cy="8" rx="3" ry="6.5"/><path d="M1.5 8h13M2.5 4.5h11M2.5 11.5h11"/></g></svg>www.nordlichtag.com</li>
    </ul>
  </section>
</main>
</body>
</html>
```